Payment company requires web design

We need a web design for a new company based in Singapore.

The company focuses on providing 2 key products: 1) an alternative payment option (i.e. like zorbu or plendrixon options) on the traditional checkout process 2) a replacement/outsource of a merchants payment page. Key in the UX flow is a end customer dashboard that manages all payments.

We look to provide a simple, fluid and easy to use payment process. The dashboard is minimalistic that allows easy navigation, review of transactions and all available options through gamification.

The final design should communicate ease of use, flexibility and transparency.

The value is for the merchant - retail/travel/insurance companies. However its the merchant's end customers that are the target and who the UX is built for.

It Company

malvri

5+ page

ec1f27

• 7 pages mimicking UX flow
• payment page * 2 - 1) alternative payment type 2) outsource of merchants payment page to our business
• our landing page
• end customer verification page
• end customer registration
• customer dashboard
• UX flow in attached file
• open to ideas
• have asked for the logo to be added
• logo to have the colour red (chinese for prosperity)
• the company is all about flexibility, transparency in personal finance management with the option of instalment payments

```html
<!DOCTYPE html>
<html lang="en">
<head>
<meta charset="utf-8">
<title>malvri — Payment Processing</title>
<link href="https://fonts.googleapis.com/css2?family=Montserrat:wght@300;400;500;700;800&display=swap" rel="stylesheet">
<style>
  :root {
    --brand-red: #ec1f27;
    --ink: #222222;
    --body-text: #333333;
    --white: #ffffff;
    --hero-top: #b9bcbf;
    --hero-mid: #a8adb2;
    --hero-bottom: #d9dadb;
  }
  * { margin: 0; padding: 0; box-sizing: border-box; }
  html, body { width: 1200px; height: 1185px; overflow: hidden; }
  body {
    font-family: "Montserrat", Arial, sans-serif;
    background: var(--white);
    color: var(--body-text);
    position: relative;
  }
  .hero {
    position: absolute; left: 0; top: 0; width: 1200px; height: 634px;
    overflow: hidden;
  }
  .hero-photo {
    position: absolute; inset: 0;
    background:
      radial-gradient(ellipse at 78% 40%, #cdc6c0 0%, rgba(205,198,192,0) 45%),
      radial-gradient(ellipse at 45% 55%, #c4c6c9 0%, rgba(196,198,201,0) 40%),
      linear-gradient(180deg, var(--hero-top) 0%, var(--hero-mid) 55%, var(--hero-bottom) 100%);
  }
  .site-nav {
    position: absolute; left: 0; top: 0; width: 1200px; height: 94px;
    border-bottom: 1px solid rgba(255,255,255,0.25);
  }
  .brand {
    position: absolute; left: 132px; top: 27px;
    font-weight: 800; font-size: 36px; color: var(--white); letter-spacing: -0.5px;
  }
  .nav-link {
    position: absolute; top: 40px; font-size: 13px; font-weight: 500; color: var(--white);
  }
  .login {
    position: absolute; left: 933px; top: 35px; width: 70px; height: 28px;
    border: 1px solid rgba(255,255,255,0.7);
    display: flex; align-items: center; justify-content: center;
    font-size: 13px; font-weight: 500; color: var(--white);
  }
  .hero-copy { position: absolute; left: 132px; top: 220px; color: var(--white); }
  .hero-kicker { font-size: 35px; font-weight: 400; line-height: 1; }
  .hero-title { font-size: 50px; font-weight: 700; line-height: 1; margin-top: 8px; }
  .hero-sub { font-size: 27px; font-weight: 400; line-height: 1; margin-top: 14px; }
  .cta {
    position: absolute; left: 133px; top: 386px; width: 146px; height: 41px;
    background: var(--brand-red); color: var(--white);
    display: flex; align-items: center; justify-content: center;
    font-size: 17px; font-weight: 400; border-radius: 2px;
  }
  .slide-prev {
    position: absolute; left: 45px; top: 275px; width: 44px; height: 44px;
    border-radius: 50%; background: rgba(150,150,150,0.45);
  }
  .slide-next { position: absolute; left: 1125px; top: 280px; }
  .faq-title {
    position: absolute; left: 0; width: 1118px; top: 660px; text-align: center;
    font-size: 38px; font-weight: 300; color: var(--ink);
  }
  .faq-line {
    position: absolute; left: 133px; font-size: 11.5px; line-height: 21.5px; width: 880px;
    color: var(--body-text);
  }
  .faq-line .tag { color: var(--brand-red); }
  .faq-line .indent { display: block; padding-left: 22px; }
  .site-footer {
    position: absolute; left: 0; top: 1114px; width: 1200px; height: 71px;
    background: var(--brand-red);
  }
  .site-footer p {
    position: absolute; left: 132px; top: 24px; font-size: 14px; color: var(--white);
  }
</style>
</head>
<body>
  <header class="hero">
    <div class="hero-photo" role="img" aria-label="Photo of three business colleagues smiling at a desk with a laptop in a bright office"></div>
    <nav class="site-nav">
      <div class="brand">malvri</div>
      <span class="nav-link" style="left:512px">About</span>
      <span class="nav-link" style="left:580px">Services</span>
      <span class="nav-link" style="left:659px">Web</span>
      <span class="nav-link" style="left:718px">Technology</span>
      <span class="nav-link" style="left:818px">Contact Us</span>
      <span class="login">Login</span>
      <span class="nav-link" style="left:1022px">Sign Up</span>
    </nav>
    <div class="slide-prev">
      <svg width="44" height="44" viewBox="0 0 44 44"><polyline points="25,8 15,22 25,36" fill="none" stroke="#fff" stroke-width="1.2"/></svg>
    </div>
    <svg class="slide-next" width="20" height="34" viewBox="0 0 20 34"><polyline points="4,2 16,17 4,32" fill="none" stroke="#fff" stroke-width="1.2"/></svg>
    <div class="hero-copy">
      <div class="hero-kicker">We are payment</div>
      <div class="hero-title">Processing Company</div>
      <div class="hero-sub">from Singapore</div>
    </div>
    <a class="cta">Register Now!</a>
  </header>

  <h2 class="faq-title">FAQ</h2>

  <p class="faq-line" style="top:722px"><span class="tag">Q:-</span> Quis autem vel eum iure reprehenderit qui in ea voluptate velit esse quam nihil molestiae consequatur, vel illum qui dolorem<span class="indent">eum fugiat quo voluptas nulla &nbsp; pariatur?</span></p>
  <p class="faq-line" style="top:778px;width:920px"><span class="tag">A:-</span> But I must explain to you how all this mistaken idea of denouncing pleasure and praising pain was born and I will give you a complete Nemo enim ipsam<span class="indent">&nbsp;voluptatem quia &nbsp;&nbsp; voluptas sit aspernatur aut odit aut fugit, sed quia consequuntur magni dolores eos qui ratione voluptatem sequi nesciunt</span></p>
  <p class="faq-line" style="top:858px"><span class="tag">Q:-</span> Ut enim ad minima veniam, quis nostrum exercitationem ullam corporis suscipit laboriosam, nisi ut aliquid ex ea commodi consequatur?</p>
  <p class="faq-line" style="top:898px;width:920px"><span class="tag">A:-</span> At vero eos et accusamus et iusto odio dignissimos ducimus qui blanditiis praesentium voluptatum deleniti atque corrupti quos dolores et quas molestias<span class="indent">excepturi sint occaecati cupiditate non provident, similique sunt in culpa qui officia deserunt mollitia animi, id est laborum et dolorum fuga.</span></p>
  <p class="faq-line" style="top:986px"><span class="tag">Q:-</span> Who chooses to enjoy a pleasure that has no annoying consequences, or one who avoids a pain that produces no resultant pleasure?</p>
  <p class="faq-line" style="top:1026px;width:920px"><span class="tag">A:-</span> Nam libero tempore, cum soluta nobis est eligendi optio cumque nihil impedit quo minus id quod maxime placeat facere possimus, omnis voluptas<span class="indent">assumenda est, omnis dolor repellendus.</span></p>

  <footer class="site-footer">
    <p>© 2016 malvri . All right reserved &nbsp;Term of Use</p>
  </footer>
</body>
</html>
```